Brindle Offers is an online marketing platform.

A daily deals site for consumers a way to bring in new clients for clients and this is who the business cards are for. Industries - Food and Drink, Things To Do, Beauty and Spas, Staycations and Services.
Logo on one side.
Name - Owen Radley
Job Title - Sales Director
Phone Number - 07912358046
Email - owen@brindleoffers.co.uk
need same for second person
Name - Fiona Bracken
Job Title - Operations Director
Phone Number - 01632840275
Email - fiona@brindleoffers.co.uk
Bottom Right - Chatterbook Icon, Snapa Icon, Pipline Icon
Target Market(s)
Business owners of the above industries
Contact Information for Business Card
Name - Owen Radley
Name - Fiona Bracken
Look and feel

```html
<!DOCTYPE html>
<html lang="en">
<head>
<meta charset="utf-8">
<title>Brindle Offers – Business Cards</title>
<link rel="stylesheet" href="https://fonts.googleapis.com/css2?family=Montserrat:wght@300;400;600;700&display=swap">
<style>
  :root {
    --backdrop: #2b2c30;
    --card: #0b0b0c;
    --ink: #f4f4f4;
    --ink-soft: #d9d9d9;
    --tab: #ececec;
    --tab-ink: #1a1a1a;
  }
  * { box-sizing: border-box; margin: 0; padding: 0; }
  html, body {
    width: 1200px;
    height: 900px;
    overflow: hidden;
    background: var(--backdrop);
    font-family: "Montserrat", Arial, sans-serif;
  }
  .stage {
    width: 1200px;
    height: 900px;
    display: flex;
    align-items: center;
    justify-content: center;
    gap: 60px;
  }
  .stage__column {
    display: flex;
    flex-direction: column;
    gap: 40px;
  }
  .card {
    position: relative;
    width: 460px;
    height: 274px;
    background: var(--card);
    border-radius: 24px;
    color: var(--ink);
    overflow: hidden;
  }

  /* Contact side */
  .contact {
    display: flex;
    flex-direction: column;
    justify-content: flex-start;
    padding: 46px 0 0 84px;
  }
  .contact__company {
    font-weight: 700;
    font-size: 17px;
    letter-spacing: 1.5px;
    text-transform: uppercase;
    margin-bottom: 22px;
    margin-left: 36px;
  }
  .contact__name {
    font-weight: 700;
    font-size: 17px;
    letter-spacing: 1px;
    text-transform: uppercase;
  }
  .contact__role {
    font-weight: 400;
    font-size: 11px;
    letter-spacing: 0.5px;
    text-transform: uppercase;
    color: var(--ink-soft);
    margin-bottom: 12px;
  }
  .contact__line {
    font-weight: 400;
    font-size: 14px;
    letter-spacing: 0.8px;
    text-transform: uppercase;
    line-height: 1.55;
  }
  .social-tab {
    position: absolute;
    right: 0;
    bottom: 18px;
    padding: 8px 14px;
    background: var(--tab);
    border-radius: 12px 0 0 12px;
    color: var(--tab-ink);
    list-style: none;
    display: flex;
    gap: 12px;
  }
  .social-tab__item {
    display: flex;
    align-items: center;
    gap: 5px;
    font-size: 10px;
    font-weight: 600;
    letter-spacing: 0.3px;
  }
  .social-tab__dot {
    width: 8px;
    height: 8px;
    border-radius: 50%;
    background: var(--tab-ink);
    flex: none;
  }

  /* Brand side */
  .brand {
    display: flex;
    flex-direction: column;
    align-items: center;
    justify-content: center;
  }
  .brand__mark {
    width: 34px;
    height: 34px;
    border-radius: 50%;
    background: var(--ink);
    margin-bottom: 20px;
  }
  .brand__name {
    font-weight: 400;
    font-size: 24px;
    letter-spacing: 8px;
    text-transform: uppercase;
    text-align: center;
    line-height: 1.35;
  }
</style>
</head>
<body>
  <main class="stage">
    <div class="stage__column">
      <section class="card contact" aria-label="Contact side, Owen Radley">
        <p class="contact__company">Brindle . Offers</p>
        <p class="contact__name">Owen Radley</p>
        <p class="contact__role">Sales Director</p>
        <p class="contact__line">07912358046</p>
        <p class="contact__line">owen@brindleoffers.co.uk</p>
        <ul class="social-tab" aria-label="Social channels">
          <li class="social-tab__item"><span class="social-tab__dot"></span>Chatterbook</li>
          <li class="social-tab__item"><span class="social-tab__dot"></span>Snapa</li>
          <li class="social-tab__item"><span class="social-tab__dot"></span>Pipline</li>
        </ul>
      </section>

      <section class="card contact" aria-label="Contact side, Fiona Bracken">
        <p class="contact__company">Brindle . Offers</p>
        <p class="contact__name">Fiona Bracken</p>
        <p class="contact__role">Operations Director</p>
        <p class="contact__line">01632840275</p>
        <p class="contact__line">fiona@brindleoffers.co.uk</p>
        <ul class="social-tab" aria-label="Social channels">
          <li class="social-tab__item"><span class="social-tab__dot"></span>Chatterbook</li>
          <li class="social-tab__item"><span class="social-tab__dot"></span>Snapa</li>
          <li class="social-tab__item"><span class="social-tab__dot"></span>Pipline</li>
        </ul>
      </section>
    </div>

    <section class="card brand" aria-label="Brand side">
      <span class="brand__mark" aria-hidden="true"></span>
      <p class="brand__name">Brindle<br>Offers</p>
    </section>
  </main>
</body>
</html>
```